Guaranteed Job - Sleek Sexy Business Card UV Spot

Im looking for a sleek and sexy business card, that resembles elite or VIP status status.
our business is corinvale.example
you can view our products on there, but our main audience for handing out our cards will be for people in the hospitality industry, so it will need to impress high management and CEO of hotels and restaurants, bars, clubs etc...
the card features will have UV spot on both sides, 400gsm stock. standard size.
Artwork should be 86 x 54mm + 2mm bleed = 90 x 58mm
it should have a nice "unique" uv spot pattern that highlights the card, not a repeated pattern, theres no originality there, and it will be disregarded.
The written material will be:
Corin Vale Hospitality College (logo)
Tobin Marsh
Director
Phone: 1300 615 737
Mobile: 0455 817 296
Email: info@corinvale.example
website: www.corinvale.example
I'm looking for originality here, i don't want just a simple stock card, want something that has a wow factor for people.
You will find the logo attached. you may invert the white to black words to suit the background as you please.
thank you and good luck
As a side note, ive received a lot of proposals, im too busy to give feedback to each and every one, so if i havent provided feedback for your design within 24 hours, then consider it not acceptable, and you could resubmit another design.
So far i have not seen any design that stood out for me, they all seem pretty generic. there nothing thats unique, i would figure for the amount that im offering, that people would put some more effort and creativity into the design.
so far over 200 designs submitted, and nothing i have seen looks very original, everything looks like a different variation of the same stuff, i said it very clearly i wanted something unique, the only thing that has come close to it so far is this one
Reason: Ive received alot of design concepts and i have reviewed everyone, but i havent had time to give feedback to every single one, only the ones that have interested me, if i havent responded, its because i havent found it good enough.
so far only a few design have been on par with what ive been looking for, an attractive eye popping design.
heres a few of them,
http://files.pixelbazaar.example/design_img/51736/62418/62418_2840915_51736_image.jpg
http://files.pixelbazaar.example/design_img/51736/68254/68254_2841377_51736_image.jpg
theyre, both unique and original, and eye catching, the only thing theyre missing is the sexyness.
if you still think you have some creativity left in your minds, then throw it on here.
Reason: Sorry guys for the delay, I was in a serious accident and out of commission for the past few months, I'm just slowly recovering now, please bare with me as i try to attend to this project, it may take me awhile as I have other projects that are on standby, I'm not 100% at the moment, so im extending the deadline for 2 weeks right now. Thanks for your patience.
Hospitality

```html
<!DOCTYPE html>
<html lang="en">
<head>
<meta charset="utf-8">
<title>Corin Vale Hospitality College – Business Card</title>
<link rel="stylesheet" href="https://fonts.googleapis.com/css2?family=Oswald:wght@500;600&family=Open+Sans:wght@400;600&display=swap">
<style>
  :root {
    --backdrop: #3a3a3c;
    --card-black: #151517;
    --card-black-edge: #222226;
    --accent-blue: #4ea3e0;
    --sky-blue: #5aaef0;
    --sky-blue-deep: #3f96dc;
    --emboss-shadow: rgba(20, 70, 120, 0.45);
    --emboss-light: rgba(200, 230, 255, 0.35);
    --text-white: #f2f2f2;
    --spot-gloss: rgba(255, 255, 255, 0.07);
  }
  * { box-sizing: border-box; margin: 0; padding: 0; }
  html, body { width: 1200px; height: 716px; overflow: hidden; }
  body {
    background: var(--backdrop);
    font-family: "Open Sans", Arial, sans-serif;
    position: relative;
  }
  .card {
    position: absolute;
    top: 190px;
    width: 520px;
    height: 336px;
    border-radius: 4px;
    overflow: hidden;
    box-shadow: 0 10px 24px rgba(0,0,0,0.45);
  }
  /* Front side */
  .card-front {
    left: 50px;
    background: linear-gradient(135deg, var(--card-black-edge), var(--card-black));
  }
  .spot-uv-mark {
    position: absolute;
    left: 290px;
    top: 70px;
    width: 170px;
    height: 170px;
    background: var(--spot-gloss);
    border-radius: 2px;
  }
  .brand {
    position: absolute;
    left: 34px;
    top: 40px;
    display: flex;
    align-items: center;
    gap: 12px;
  }
  .brand-square {
    width: 44px;
    height: 44px;
    background: var(--accent-blue);
  }
  .brand-name {
    font-family: "Oswald", "Arial Narrow", sans-serif;
    font-weight: 500;
    font-size: 17px;
    line-height: 1.1;
    color: var(--text-white);
    text-transform: uppercase;
    letter-spacing: 0.5px;
    width: 160px;
  }
  .person {
    position: absolute;
    left: 146px;
    top: 128px;
  }
  .person-name {
    font-size: 19px;
    color: var(--accent-blue);
    text-transform: uppercase;
    letter-spacing: 0.5px;
  }
  .person-role {
    font-size: 16px;
    color: var(--text-white);
    margin-top: 2px;
  }
  .mobile {
    display: flex;
    align-items: center;
    gap: 10px;
    margin-top: 6px;
    margin-left: -18px;
    font-size: 14px;
    color: var(--text-white);
  }
  .contact-list {
    position: absolute;
    left: 146px;
    top: 246px;
    list-style: none;
  }
  .contact-list li {
    display: flex;
    align-items: center;
    gap: 10px;
    margin-left: -18px;
    font-size: 14px;
    line-height: 22px;
    color: var(--text-white);
  }
  .icon { width: 10px; height: 10px; flex: none; }
  .icon path, .icon rect, .icon circle { fill: none; stroke: var(--accent-blue); stroke-width: 1.4; }
  .icon .solid { fill: var(--accent-blue); stroke: none; }

  /* Back side */
  .card-back {
    left: 630px;
    background: linear-gradient(160deg, var(--sky-blue), var(--sky-blue-deep));
  }
  .back-title {
    position: absolute;
    left: 40px;
    top: 70px;
    font-family: "Oswald", "Arial Narrow", sans-serif;
    font-weight: 600;
    text-transform: uppercase;
    color: var(--sky-blue);
    text-shadow: -1px -1px 0 var(--emboss-light), 1px 1px 1px var(--emboss-shadow);
    line-height: 0.98;
  }
  .back-title .line-main { display: block; font-size: 58px; letter-spacing: 1px; }
  .back-title .line-sub { display: block; font-size: 27px; letter-spacing: 1.5px; margin-top: 4px; }
  .back-web {
    position: absolute;
    left: 40px;
    bottom: 30px;
    font-size: 13px;
    color: #0e2a40;
    letter-spacing: 0.3px;
  }
</style>
</head>
<body>
  <section class="card card-front" aria-label="Business card front">
    <div class="spot-uv-mark" role="img" aria-label="Spot UV gloss area for the college mark"></div>
    <div class="brand">
      <span class="brand-square"></span>
      <span class="brand-name">Corin Vale Hospitality College</span>
    </div>
    <div class="person">
      <p class="person-name">Tobin Marsh</p>
      <p class="person-role">Director</p>
      <p class="mobile">
        <svg class="icon" viewBox="0 0 10 10" aria-hidden="true"><rect x="2.5" y="0.8" width="5" height="8.4" rx="1"/></svg>
        0455 817 296
      </p>
    </div>
    <ul class="contact-list">
      <li>
        <svg class="icon" viewBox="0 0 10 10" aria-hidden="true"><circle class="solid" cx="5" cy="5" r="5"/></svg>
        1300 615 737
      </li>
      <li>
        <svg class="icon" viewBox="0 0 10 10" aria-hidden="true"><rect class="solid" x="0" y="1.5" width="10" height="7" rx="1"/></svg>
        info@corinvale.example
      </li>
      <li>
        <svg class="icon" viewBox="0 0 10 10" aria-hidden="true"><circle cx="5" cy="5" r="4.2"/><path d="M0.8 5h8.4M5 0.8v8.4"/></svg>
        www.corinvale.example
      </li>
    </ul>
  </section>

  <section class="card card-back" aria-label="Business card back">
    <h1 class="back-title">
      <span class="line-main">Corin</span>
      <span class="line-main">Vale</span>
      <span class="line-sub">Hospitality College</span>
    </h1>
    <p class="back-web">www.corinvale.example</p>
  </section>
</body>
</html>
```